Attractive Flyer for Moving Company

Our Company called "Bluecrest Moving Company".
We provide moving service for home and businesses
We need a flyer for a moving company, located in San Diego, CA USA
Flyer size will be 7 x 5 inches, double sided.

Flyer needs to be very attractive and catchy for eye. I want people to keep it even if they dont need our service. I attached a lot of text in separate word file.
Logo, brief and additional pictures are attached.

Target Market(s)

27 years - 55 Years old

Industry/Entity Type

Moving Company

Colors
ec1f27
3176b5
ffffff

Requirements
Must have
• Attached in Word File
Nice to have
• Please be creative in placing a text and selecting a back ground picture.

```html
<!DOCTYPE html>
<html lang="en">
<head>
<meta charset="utf-8">
<title>Bluecrest Moving Company – Your Special Deal</title>
<link rel="stylesheet" href="https://fonts.googleapis.com/css2?family=Oswald:wght@500;600;700&family=Open+Sans:wght@700;800&display=swap">
<style>
  :root {
    --red: #be1e2d;
    --blue: #1f3f7a;
    --white: #ffffff;
    --yellow: #fff200;
    --display: "Oswald", "Arial Narrow", sans-serif;
    --body: "Open Sans", Arial, sans-serif;
  }
  * { margin: 0; padding: 0; box-sizing: border-box; }
  html, body { width: 858px; height: 1200px; overflow: hidden; background: var(--white); }
  .flyer { position: relative; width: 858px; height: 1200px; overflow: hidden; background: var(--white); }
  .flyer-shapes { position: absolute; inset: 0; width: 858px; height: 1200px; }

  .brand-name {
    position: absolute; left: 34px; top: 72px; width: 300px;
    font-family: var(--display); font-weight: 700; color: var(--red);
    text-transform: uppercase; line-height: 1; text-align: center;
  }
  .brand-name .brand-main { display: block; font-size: 50px; letter-spacing: 1px; }
  .brand-name .brand-sub { display: block; font-size: 22px; letter-spacing: 3px; margin-top: 4px; }

  .deal-heading {
    position: absolute; left: 366px; top: 80px; width: 400px; text-align: center;
    font-family: var(--display); font-weight: 600; color: var(--white);
    font-size: 47px; line-height: 1; white-space: nowrap;
  }
  .deal-note {
    position: absolute; left: 366px; top: 131px; width: 400px; text-align: center;
    font-family: var(--body); font-weight: 700; color: var(--white);
    font-size: 15px; line-height: 17px; white-space: nowrap;
  }

  .offers {
    position: absolute; left: 97px; top: 268px; width: 600px;
    list-style: none; text-align: center;
    font-family: var(--display); font-weight: 600; color: var(--white);
    text-transform: uppercase; line-height: 44px; white-space: nowrap;
  }
  .offers li { font-size: 34px; margin-bottom: 17px; }
  .offers li:first-child { margin-bottom: 11px; }
  .offers .figure { font-size: 41px; }

  .included-heading {
    position: absolute; left: 125px; top: 692px;
    font-family: var(--display); font-weight: 600; color: var(--white);
    font-size: 49px; line-height: 1; text-transform: uppercase; white-space: nowrap;
  }
  .included-list {
    position: absolute; left: 125px; top: 780px; width: 640px; list-style: none;
    font-family: var(--body); font-weight: 700; color: var(--white);
    font-size: 20.5px; line-height: 25px; white-space: nowrap;
  }
  .included-list li { margin-bottom: 13px; }

  .voucher-text { font-family: var(--body); font-weight: 800; fill: var(--red); }
</style>
</head>
<body>
<main class="flyer">
  <svg class="flyer-shapes" viewBox="0 0 930 1300" preserveAspectRatio="none" aria-hidden="true">
    <polygon class="frame-blue" fill="var(--blue)" points="0,0 855,50 855,1245 0,1300"/>
    <polygon class="panel-red" fill="var(--red)" points="340,28 830,72 830,1228 0,1292 0,225"/>
    <polygon class="corner-stripe" fill="var(--blue)" points="0,0 345,28 440,198 0,226"/>
    <polygon class="corner-white" fill="var(--white)" points="0,0 330,26 418,186 0,214"/>
    <g class="voucher-badge" transform="translate(425 1132) rotate(-7)">
      <polygon fill="var(--yellow)" points="200,0 169,10 188,27 149,30 153,50 111,46 100,68 59,56 35,77 0,60 -35,77 -59,56 -100,68 -111,46 -153,50 -149,30 -188,27 -169,10 -200,0 -169,-10 -188,-27 -149,-30 -153,-50 -111,-46 -100,-68 -59,-56 -35,-77 0,-60 35,-77 59,-56 100,-68 111,-46 153,-50 149,-30 188,-27 169,-10"/>
      <text class="voucher-text" x="0" y="-12" text-anchor="middle" font-size="20">Keep this voucher it is valid until</text>
      <text class="voucher-text" x="0" y="30" text-anchor="middle" font-size="39">January 1st 2019</text>
    </g>
  </svg>

  <div class="brand-name">
    <span class="brand-main">Bluecrest</span>
    <span class="brand-sub">Moving Company</span>
  </div>

  <h1 class="deal-heading">YOUR SPECIAL DEAL</h1>
  <p class="deal-note">(Cannot be used with any other promotions<br>or coupons)</p>

  <ul class="offers">
    <li>Save <span class="figure">15%</span> -<span class="figure">25%</span> on your move</li>
    <li><span class="figure">$235</span> – <span class="figure">3</span> hours of moving service<br>with <span class="figure">2</span> pro movers</li>
    <li><span class="figure">$325</span> - <span class="figure">3</span> hours of moving service<br>with <span class="figure">3</span> pro movers</li>
    <li>+ <span class="figure">20%</span> off for boxes and packing<br>supplies.</li>
  </ul>

  <h2 class="included-heading">Included in price</h2>
  <ul class="included-list">
    <li>Protection of your furniture with specialized blankets<br>and plastic wrap.</li>
    <li>Dis-assembly and reassembly of your furniture.</li>
    <li>Wardrobe boxes for the duration of moving process.</li>
  </ul>
</main>
</body>
</html>
```